Redesign of 3-4 page site for professional services firm

Our site is www.kestrelvaleadvisors.com. We currently have a simple page made with HostNimbo tools. But the tools are not able to generate the look and feel we desire. We need a home page similar to current that tells a little about our company, our experience and our team. We need a second page to show details of current and past transactions we have assisted our clients with. Currently this page reads like a word document but we would like for it to present in a cleaner fashion and liven it up with some images that link to the industry served. For example, a motorcycle outline in a circle for the powersports related transactions. We would like page to introduce each member of "Our Team" and highlight their experience with a photo of each person. If there is no photo available, we would like a placeholder to be their initials in a circle that can be updated later. We would also like a contact us section whether this is a different page or part of the home page.

Target Market(s)

Retirement minded business owners

Industry/Entity Type

Professional Services

Coding

Coded - Design and coding required

Requirements
Must have
• See project description. Must include a page or section for "Current Listings" and "Recently Completed Transactions" (can be same page)

```html
<!DOCTYPE html>
<html lang="en">
<head>
<meta charset="utf-8">
<title>Kestrel Vale Advisors — Strategically Navigating Business Exits</title>
<link rel="stylesheet" href="https://fonts.googleapis.com/css2?family=Roboto+Condensed:wght@700&family=Montserrat:wght@400;500;600;700&display=swap">
<style>
:root{
  --green:#14b014;
  --lime:#8cc63f;
  --olive:#b2ad00;
  --red:#e2231a;
  --yellow:#e6c41c;
  --ink:#111;
  --text:#333;
  --muted:#555;
  --soft:#f4f4f4;
  --line:#cfcfcf;
}
*{margin:0;padding:0;box-sizing:border-box}
html,body{width:1200px;height:4222px;overflow:hidden}
body{font-family:"Montserrat",sans-serif;color:var(--text);background:#fff;position:relative}
.abs{position:absolute}
h1,h2,h3{font-family:"Roboto Condensed",sans-serif;font-weight:700;color:var(--ink)}
.btn{position:absolute;background:var(--green);color:#fff;font-family:"Montserrat",sans-serif;font-weight:600;font-size:14px;text-transform:uppercase;display:flex;align-items:center;justify-content:center;letter-spacing:.2px}
.divider{position:absolute;display:flex;gap:6px;height:3px}
.divider span{width:20px;height:3px;display:block}
.divider span:nth-child(1){background:var(--red)}
.divider span:nth-child(2){background:var(--yellow)}
.divider span:nth-child(3){background:var(--green)}
.divider.center{left:50%;transform:translateX(-50%)}
.brand{position:absolute;display:flex;align-items:center;gap:10px;font-family:"Montserrat",sans-serif;font-weight:600;color:#333;letter-spacing:.5px}
.brand .dot{background:var(--green);border-radius:50%}

/* header */
.site-header{position:absolute;left:0;top:0;width:1200px;height:121px;background:#fff}
.call-badge{position:absolute;left:836px;top:0;width:364px;height:49px;background:var(--lime);border-bottom-left-radius:40px;color:#fff;display:flex;align-items:center;padding-left:54px;gap:12px}
.call-badge .ring{width:34px;height:34px;border:2px solid #fff;border-radius:50%;display:flex;align-items:center;justify-content:center}
.call-badge small{display:block;font-size:12px;line-height:1.1}
.call-badge b{font-weight:500;font-size:14px}
.main-nav{position:absolute;top:89px;left:637px;display:flex;gap:42px;font-size:12px;text-transform:uppercase;color:#333}
.main-nav .active{font-weight:700;color:#000}

/* hero */
.hero{position:absolute;left:0;top:121px;width:1200px;height:625px}
.hero-photo{position:absolute;inset:0;background:linear-gradient(160deg,#8a98a0 0%,#75858e 45%,#67767f 100%)}
.hero h1{position:absolute;left:144px;top:226px;font-size:50px;line-height:59px;color:#111}
.hero .btn{left:144px;top:354px;width:125px;height:39px}
.hero-edge{position:absolute;left:0;bottom:0;width:1200px;height:130px}

/* about */
.about-frame{position:absolute;left:126px;top:793px;width:408px;height:335px;border:2px solid var(--red)}
.about-photo{position:absolute;left:141px;top:803px;width:405px;height:410px;background:linear-gradient(135deg,#4a3a2e,#6b5443 50%,#8c7461)}
.about h2{position:absolute;left:595px;top:838px;font-size:39px}
.about p{position:absolute;left:595px;width:468px;font-size:11.5px;line-height:23px;color:#222}
.about .lead{top:920px;font-weight:500}
.about .body{top:992px}

/* experience */
.section-title{position:absolute;left:0;width:1200px;text-align:center;font-size:39px}
.exp-card{position:absolute;width:401px;height:113px;background:#fff;box-shadow:0 1px 6px rgba(0,0,0,.15);display:flex;align-items:center;padding:0 20px 0 18px;gap:22px}
.exp-icon{flex:0 0 52px;height:52px;border-radius:50%;background:radial-gradient(circle,#e9f6e3,#f7f7f7)}
.exp-card p{font-size:11px;line-height:20px;color:#222}

/* team */
.team-band{position:absolute;left:0;top:1800px;width:1200px;height:732px;background:var(--soft)}
.team-intro{position:absolute;left:165px;top:1940px;width:870px;text-align:center;font-size:11.5px;line-height:23px;color:#222}
.member{position:absolute;top:2050px;width:240px;text-align:center}
.member .photo{width:214px;height:214px;border-radius:50%;margin:0 auto;background:linear-gradient(180deg,#cfcfcf 0%,#b9b9b9 60%,#2a2f3a 100%)}
.member h3{font-family:"Montserrat",sans-serif;font-weight:600;font-size:13.5px;margin-top:24px;color:#111}
.member span{display:block;font-size:11px;margin-top:8px;color:#333}

/* testimonials */
.quote-card{position:absolute;top:2695px;width:282px;height:231px;background:#fff;border:1px solid #e2e2e2;padding:20px 20px}
.quote-card p{font-size:11px;line-height:21.5px;color:#444}
.quote-card hr{border:0;border-top:1px solid #ddd;margin:14px 0 14px}
.quote-card h4{font-weight:500;font-size:12px;color:#1c2c6b}
.stars{color:var(--yellow);font-size:10px;letter-spacing:1px}
.arrow{position:absolute;top:2790px}

/* newsletter */
.newsletter{position:absolute;left:0;top:3065px;width:1200px;height:341px;background:var(--soft)}
.newsletter p{position:absolute;left:340px;top:146px;width:580px;text-align:center;font-size:11.5px;line-height:23px;color:#222}
.email-field{position:absolute;left:338px;top:202px;width:452px;height:41px;background:#fff;border:1px solid #bbb;font-size:10.5px;padding:0 18px;display:flex;align-items:center;color:#333}

/* contact */
.contact{position:absolute;left:0;top:3406px;width:1200px;height:770px}
.contact-photo{position:absolute;inset:0;background:linear-gradient(180deg,#2e3540 0%,#556068 40%,#6f6a5a 100%)}
.contact h2{position:absolute;left:0;top:82px;width:1200px;text-align:center;font-size:39px;color:#fff}
.contact .intro{position:absolute;left:170px;top:150px;width:860px;text-align:center;color:#fff;font-size:12px;line-height:24px}
.contact-box{position:absolute;left:184px;top:229px;width:832px;height:446px;background:#fff;display:flex}
.contact-info{width:416px;padding:0 36px;position:relative}
.contact-info p{position:absolute;left:32px;top:198px;width:340px;font-size:11.5px;line-height:21px;color:#222}
.info-row{position:absolute;left:32px;display:flex;align-items:center;gap:20px;font-size:12px;line-height:21px;color:#222}
.info-row .ic{width:34px;height:34px;border-radius:50%;display:flex;align-items:center;justify-content:center}
.inquiry{width:416px;position:relative}
.inquiry h3{position:absolute;left:36px;top:50px;font-size:21px}
.field{position:absolute;left:36px;width:338px;border-bottom:1px solid #bbb;height:26px;display:flex;gap:10px;font-size:11.5px;color:#222;align-items:flex-start}
.site-footer{position:absolute;left:0;top:4176px;width:1200px;height:46px;background:var(--green);color:#fff;font-size:12px}
.site-footer .copy{position:absolute;left:144px;top:15px}
.footer-nav{position:absolute;left:778px;top:17px;display:flex;gap:52px}
</style>
</head>
<body>

<header class="site-header">
  <div class="brand" style="left:141px;top:44px;font-size:28px">
    <span class="dot" style="width:16px;height:16px"></span>Kestrel Vale
  </div>
  <div class="call-badge">
    <span class="ring"><svg width="16" height="16" viewBox="0 0 24 24" fill="none" stroke="#fff" stroke-width="2"><path d="M22 16.9v3a2 2 0 0 1-2.2 2 19.8 19.8 0 0 1-8.6-3.1 19.5 19.5 0 0 1-6-6A19.8 19.8 0 0 1 2.1 4.2 2 2 0 0 1 4.1 2h3a2 2 0 0 1 2 1.7c.1.9.4 1.8.7 2.7a2 2 0 0 1-.5 2.1L8 9.8a16 16 0 0 0 6 6l1.3-1.3a2 2 0 0 1 2.1-.4c.9.3 1.8.6 2.7.7a2 2 0 0 1 1.7 2z"/></svg></span>
    <div><small>Call Us</small><b>405-555-0142</b></div>
  </div>
  <nav class="main-nav">
    <span class="active">Home</span><span>Business Listing</span><span>Our Team</span><span>Contact Us</span>
  </nav>
</header>

<section class="hero">
  <div class="hero-photo" role="img" aria-label="Photo of chalk arrows branching in three directions on pavement in front of a pair of sneakers"></div>
  <h1>Strategically Navigating<br>Business Exits</h1>
  <div class="btn">Contact Us</div>
  <svg class="hero-edge" viewBox="0 0 1200 130" preserveAspectRatio="none">
    <path d="M0 112 L620 0 L1200 102 L1200 130 L0 130Z" fill="var(--olive)"/>
    <path d="M0 130 L620 20 L1200 116 L1200 130Z" fill="#fff"/>
    <path d="M0 130 L1200 116" stroke="var(--olive)" stroke-width="3"/>
  </svg>
</section>

<section class="about">
  <div class="about-frame"></div>
  <div class="about-photo" role="img" aria-label="Photo of a smiling business team shaking hands across a meeting table"></div>
  <h2>ABOUT OUR COMPANY</h2>
  <div class="divider" style="left:598px;top:905px"><span></span><span></span><span></span></div>
  <p class="lead">At Kestrel Vale Advisors, our mission is to empower entrepreneurs and business owners by facilitating seamless transactions that lead to mutual success</p>
  <p class="body">We understand that selling or acquiring a business can be a complex &amp; emotional journey, which is why our dedicated team of experts is here to guide you every step of the way. With a commitment to integrity, transparency, and unmatched professionalism, we strive to create a positive and rewarding experience for all our clients.</p>
  <div class="btn" style="left:595px;top:1128px;width:126px;height:41px">Contact Us</div>
</section>

<section class="experience">
  <h2 class="section-title" style="top:1282px">OUR EXPERIENCE</h2>
  <div class="divider center" style="top:1336px"><span></span><span></span><span></span></div>
  <div class="exp-card" style="left:184px;top:1362px"><div class="exp-icon" role="img" aria-label="Icon of gears and a growth chart"></div><p>With decades of experience Kestrel Vale Advisors has proudly assisted numerous clients in successfully navigating the intricate journey of selling their businesses.</p></div>
  <div class="exp-card" style="left:621px;top:1362px"><div class="exp-icon" role="img" aria-label="Icon of hands holding a lightbulb"></div><p>Our team brings a wealth of knowledge and expertise acquired through years of working closely with entrepreneurs and business owners across diverse industries.</p></div>
  <div class="exp-card" style="left:184px;top:1488px"><div class="exp-icon" role="img" aria-label="Icon of a maze"></div><p>We understand the unique challenges and complexities involved in selling a business, from valuation and marketing to negotiations and closing the deal.</p></div>
  <div class="exp-card" style="left:621px;top:1488px"><div class="exp-icon" role="img" aria-label="Icon of a head with a puzzle and lightbulb"></div><p>Our extensive experience allows us to anticipate potential obstacles and proactively find solutions, ensuring a seamless and efficient process for our clients.</p></div>
  <div class="exp-card" style="left:184px;top:1614px"><div class="exp-icon" role="img" aria-label="Icon of a document with a settings gear"></div><p>We take pride in our track record of delivering exceptional results and helping our clients achieve their desired outcomes.</p></div>
  <div class="brand" style="left:630px;top:1672px;font-size:28px"><span class="dot" style="width:16px;height:16px"></span>Kestrel Vale</div>
  <div class="btn" style="left:887px;top:1669px;width:128px;height:41px">Contact Us</div>
</section>

<section class="team">
  <div class="team-band"></div>
  <h2 class="section-title" style="top:1870px">OUR TEAM</h2>
  <div class="divider center" style="top:1924px"><span></span><span></span><span></span></div>
  <p class="team-intro">Together, our team of CPAs, attorneys, real estate brokers, and financial advisors work collaboratively to provide you with a holistic approach to business transactions. With our combined knowledge and experience, we strive to ensure a smooth and successful journey for our clients, delivering exceptional results and peace of mind.</p>
  <div class="member" style="left:126px"><div class="photo" role="img" aria-label="Portrait photo of Martin Hale"></div><h3>Martin Hale, CPA, JD</h3><span>Finance And Legal Expertise</span></div>
  <div class="member" style="left:360px"><div class="photo" role="img" aria-label="Portrait photo of Owen Pratt"></div><h3>Owen Pratt</h3><span>Vice President</span></div>
  <div class="member" style="left:596px"><div class="photo" role="img" aria-label="Portrait photo of Derek Lund"></div><h3>Derek Lund</h3><span>Powersports &amp; Automotive Industries</span></div>
  <div class="member" style="left:827px"><div class="photo" role="img" aria-label="Portrait photo of a senior team member"></div></div>
  <div class="btn" style="left:515px;top:2421px;width:131px;height:41px">Read More</div>
</section>

<section class="testimonials">
  <h2 class="section-title" style="top:2596px">HAPPY CUSTOMER WORDS</h2>
  <div class="divider center" style="top:2650px"><span></span><span></span><span></span></div>
  <svg class="arrow" style="left:106px" width="28" height="18" viewBox="0 0 28 18"><path d="M27 9H3M10 2L3 9l7 7" fill="none" stroke="#888" stroke-width="2"/></svg>
  <svg class="arrow" style="left:1060px" width="28" height="18" viewBox="0 0 28 18"><path d="M1 9h24M18 2l7 7-7 7" fill="none" stroke="var(--red)" stroke-width="2"/></svg>
  <div class="quote-card" style="left:141px"><p>Lorem ipsum dolor sit amet, consectetuer adipiscing elit, sed diam nonummy nibh euismod tincidunt ut laoreet dolore magna aliquam erat volutpat. Ut wisi nim ad minim veniam, quis nostrud exerci tation ullamnim ad minim veniam, quis.</p><hr><h4>Leon Ashby</h4><div class="stars">★★★★★</div></div>
  <div class="quote-card" style="left:457px"><p>Lorem ipsum dolor sit amet, consectetuer adipiscing elit, sed diam nonummy nibh euismod tincidunt ut laoreet dolore magna aliquam erat volutpat. Ut wisi nim ad minim veniam, quis nostrud exerci tation ullamnim ad minim veniam, quis.</p><hr><h4>Paul Greer</h4><div class="stars">★★★★★</div></div>
  <div class="quote-card" style="left:775px"><p>Lorem ipsum dolor sit amet, consectetuer adipiscing elit, sed diam nonummy nibh euismod tincidunt ut laoreet dolore magna aliquam erat volutpat. Ut wisi nim ad minim veniam, quis nostrud exerci tation ullamnim ad minim veniam, quis.</p><hr><h4>Samir Dorsey</h4><div class="stars">★★★★★</div></div>
  <div class="btn" style="left:536px;top:2954px;width:126px;height:41px">Contact Us</div>
</section>

<section class="newsletter">
  <h2 class="section-title" style="top:76px;left:25px">NEWSLETTER SIGN UP</h2>
  <div class="divider center" style="top:128px;margin-left:25px"><span></span><span></span><span></span></div>
  <p>Sign up to hear from us about exciting new opportunities. Enter your email below to be added to our mailing list.</p>
  <div class="email-field">Enter your email address</div>
  <div class="btn" style="left:803px;top:202px;width:115px;height:41px">Sign Up</div>
</section>

<section class="contact">
  <div class="contact-photo" role="img" aria-label="Aerial photo of a city skyline at dusk"></div>
  <h2>CONTACT US</h2>
  <p class="intro">Our team is ready to assist you. Whether you're looking for more information about our services or need help with a specific issue, don't hesitate to reach out. Fill out the form below, send us an email, or give us a call—we'll get back to you as soon as possible.</p>
  <div class="contact-box">
    <div class="contact-info">
      <div class="brand" style="left:36px;top:122px;font-size:28px"><span class="dot" style="width:16px;height:16px"></span>Kestrel Vale</div>
      <p>We &nbsp;strive to stay in communication with our clients. Have a question about &nbsp;how we can match your specific needs? Send us a &nbsp;message, or give us a call. We're always happy to meet new customers!</p>
      <div class="info-row" style="top:298px"><span class="ic" style="background:var(--red)"><svg width="14" height="18" viewBox="0 0 24 30" fill="none" stroke="#fff" stroke-width="2.5"><path d="M12 28s10-10 10-16a10 10 0 0 0-20 0c0 6 10 16 10 16z"/><circle cx="12" cy="12" r="3.5"/></svg></span><span>220 Alder Court, Linwood,<br>Oklahoma 74001, United States</span></div>
      <div class="info-row" style="top:350px"><span class="ic" style="background:#c4c22a"><svg width="15" height="15" viewBox="0 0 24 24" fill="none" stroke="#fff" stroke-width="2.2"><path d="M22 16.9v3a2 2 0 0 1-2.2 2 19.8 19.8 0 0 1-8.6-3.1 19.5 19.5 0 0 1-6-6A19.8 19.8 0 0 1 2.1 4.2 2 2 0 0 1 4.1 2h3a2 2 0 0 1 2 1.7c.1.9.4 1.8.7 2.7a2 2 0 0 1-.5 2.1L8 9.8a16 16 0 0 0 6 6l1.3-1.3a2 2 0 0 1 2.1-.4c.9.3 1.8.6 2.7.7a2 2 0 0 1 1.7 2z"/></svg></span><span>405-555-0142</span></div>
    </div>
    <div class="inquiry">
      <h3>QUICK INQUIRY</h3>
      <div class="divider" style="left:36px;top:90px"><span></span><span></span><span></span></div>
      <div class="field" style="top:126px"><svg width="14" height="14" viewBox="0 0 24 24" fill="none" stroke="var(--red)" stroke-width="2"><circle cx="12" cy="8" r="4"/><path d="M4 22c0-4.4 3.6-8 8-8s8 3.6 8 8"/></svg>Name</div>
      <div class="field" style="top:174px"><svg width="14" height="14" viewBox="0 0 24 24" fill="none" stroke="var(--red)" stroke-width="2"><rect x="2" y="5" width="20" height="14"/><path d="M2 5l10 8 10-8"/></svg>Email</div>
      <div class="field" style="top:224px"><svg width="14" height="14" viewBox="0 0 24 24" fill="none" stroke="var(--red)" stroke-width="2"><path d="M22 16.9v3a2 2 0 0 1-2.2 2 19.8 19.8 0 0 1-8.6-3.1 19.5 19.5 0 0 1-6-6A19.8 19.8 0 0 1 2.1 4.2 2 2 0 0 1 4.1 2h3a2 2 0 0 1 2 1.7c.1.9.4 1.8.7 2.7a2 2 0 0 1-.5 2.1L8 9.8a16 16 0 0 0 6 6l1.3-1.3a2 2 0 0 1 2.1-.4c.9.3 1.8.6 2.7.7a2 2 0 0 1 1.7 2z"/></svg>Phone</div>
      <div class="field" style="top:274px;height:50px"><svg width="14" height="14" viewBox="0 0 24 24" fill="none" stroke="var(--red)" stroke-width="2"><path d="M21 15a2 2 0 0 1-2 2H7l-4 4V5a2 2 0 0 1 2-2h14a2 2 0 0 1 2 2z"/></svg>Message</div>
      <div class="btn" style="left:36px;top:357px;width:131px;height:37px">Submit Now</div>
    </div>
  </div>
</section>

<footer class="site-footer">
  <span class="copy">© 2025 Kestrel Vale Advisors. All Rights Reserved.</span>
  <nav class="footer-nav"><span style="font-weight:600">Home</span><span>Business Listing</span><span>Our Team</span></nav>
</footer>

</body>
</html>
```